Rack Cards

We need a series of (4) Rack Card size "postcards" to have the same design but different wording. The rack cards need to include our logo and be in our branding colors (espresso brown and orangey copper.) The card needs to be double sided, with verbage on one side and our logo and jewelry pictures on the other side. Please use josefin font to match our logo. Also, please keep diamond pictures with bridal, colored stone jewelry to be dispersed between remaining cards. More jewelry pictures available upon request.
See attached files for logo, wording and jewelry pictures.
Sorry for the error in sizing. The correct size of the rack cards should be 8.27" long by 3.74" wide.
Jewelry

```html
<!DOCTYPE html>
<html lang="en">
<head>
<meta charset="utf-8">
<title>Aldenne Jewelry &amp; Design Studio – Rack Card</title>
<link rel="stylesheet" href="https://fonts.googleapis.com/css2?family=Josefin+Sans:ital,wght@0,300;0,400;0,600;1,400;1,600&display=swap">
<style>
  :root {
    --canvas: #e9e8ec;
    --paper: #ffffff;
    --espresso: #2b1a12;
    --copper: #c97a3c;
    --copper-soft: #c98449;
    --ink: #2a1d17;
    --placeholder-light: #f4f4f6;
    --placeholder-dark: #e4e4e9;
  }
  * { box-sizing: border-box; margin: 0; padding: 0; }
  html, body {
    width: 1200px; height: 900px; overflow: hidden;
    background: var(--canvas);
    font-family: "Josefin Sans", sans-serif;
  }
  .canvas { position: relative; width: 1200px; height: 900px; }

  .rack-card { position: absolute; }

  /* Front */
  .card-front {
    left: 290px; top: 91px; width: 321px; height: 711px;
    background: var(--paper);
  }
  .brand {
    position: absolute; top: 198px; left: 0; width: 100%;
    text-align: center; color: var(--ink);
  }
  .brand-name {
    font-weight: 300; font-size: 54px; letter-spacing: 1px; line-height: 1;
  }
  .brand-tagline {
    margin-top: 10px;
    font-weight: 300; font-size: 18px; letter-spacing: 0.3px;
  }
  .jewel-visual {
    position: absolute; left: 25px; top: 398px;
    width: 260px; height: 272px;
    background: linear-gradient(180deg, var(--placeholder-light), var(--placeholder-dark));
  }

  /* Back */
  .card-back {
    left: 660px; top: 97px; width: 317px; height: 700px;
    background: var(--espresso); color: var(--copper);
    padding: 24px 15px 0 15px;
  }
  .card-title {
    text-align: center; font-weight: 400; font-size: 26px;
    font-variant: small-caps; letter-spacing: 1px; line-height: 1;
    color: var(--copper-soft);
  }
  .card-body { margin-top: 14px; }
  .card-body p {
    font-weight: 300; font-size: 9.6px; line-height: 13.7px;
    text-align: justify;
  }
  .step-heading {
    margin: 11px 0 9px; font-style: italic; font-weight: 600; font-size: 11px;
    line-height: 13px;
  }
  .call-to-action {
    margin-top: 24px; text-align: center;
    font-style: italic; font-weight: 600; font-size: 13.5px; line-height: 18px;
  }
  .phone {
    margin-top: 14px; text-align: center;
    font-style: italic; font-weight: 400; font-size: 19px; letter-spacing: 0.5px;
  }
</style>
</head>
<body>
<main class="canvas">

  <section class="rack-card card-front">
    <div class="brand">
      <div class="brand-name">aldenne</div>
      <div class="brand-tagline">Jewelry &amp; Design Studio</div>
    </div>
    <div class="jewel-visual" role="img" aria-label="Jewelry rendering: hand-drawn ring with a green gemstone"></div>
  </section>

  <section class="rack-card card-back">
    <h1 class="card-title">Custom Design</h1>
    <div class="card-body">
      <p>A custom designed piece of jewelry generally takes three to four weeks from concept to completion and during the entire process, you are involved making it a true collaboration. At Aldenne’s we still produce our designs with traditional methods using ideas, pen and paper. We then fabricate in gold or wax-model by hand with meticulous care and old world craftsmanship.</p>

      <h2 class="step-heading">Tell us what jewelry you like</h2>
      <p>First we talk. Sometimes our designs start with a stone that you want to showcase and other times it’s just a broad concept like “I want a new ring.” We’ll show you various types of jewelry to find elements such as setting style and finish to determine what you like and throughout the interview we sketch out rough concepts to discover the “look” that you’re trying to achieve. Once we have a good idea of some design concepts we then produce high quality hand drawn renderings of three proposed designs.</p>

      <h2 class="step-heading">What do you think?</h2>
      <p>Once the initial renderings are complete, we sit down with you again to get your input. In most cases, one of the proposed designs will be perfect for you. If not, we’ll produce three more designs for you to view. With your help, we refine and combine design elements until we have arrived at the jewelry you’ve been dreaming about. Approve the design and then we’ll make it for you, exactly as drawn.</p>

      <h2 class="step-heading">Wax Model or Gold Mounting</h2>
      <p>The next step depends on the design. In some cases, it is more practical to produce a wax model of your design that would then be cast into gold or platinum. With other designs, it is more time efficient and cost effective to fabricate the design directly with gold or platinum. Whether we model in wax or fabricate in gold, you will be called before the job is complete so you can inspect the work done and request any last design refinements. After this final approval, the jewelry is completed, set and polished and you have…the jewelry of your dreams. You will also then be presented with the framed original rendering of your design.</p>
    </div>
    <p class="call-to-action">Call today to schedule your custom design consultation</p>
    <p class="phone">(555) 204-7731</p>
  </section>

</main>
</body>
</html>
```